National Virtual accounting firm needs website designed

I need a wordpress website design for a national virtual accounting firm. I will upload my business card, logo, and postcards that I have had designed and followed the same style. I want a similar style to be followed so I can keep the running theme similar.

Services include:

Tax Services:
Tax preparation and planning services for Individuals, businesses, estates, and nonprofits
Full Service Payroll for Businesses
ODV Audit Representation

Consulting:
Entity Selection & Restructuring
Financial Projections & Forecasts
Retirement Planning
IPO Readiness

Accounting:
Bookkeeping
Reviews and Compilations
Payroll Services

Other Services:
CFO Services
Compliance Services
Controller Services
Software Implementations for Brimlane, Corvanta, and Plivorn.

Target Market(s)

small to medium size businesses, and individuals

Industry/Entity Type

accounting firms

Font styles to use
Sans Serif

Colors
59FF00
82FF00
B8FF75
E3FFCB
F4FFEA

Requirements
Must have
• Color schematics from the logo and post cards/business cards

```html
<!DOCTYPE html>
<html lang="en">
<head>
<meta charset="utf-8">
<title>Lumora — Virtual Accounting</title>
<link href="https://fonts.googleapis.com/css2?family=Figtree:wght@400;500;600;700;800&display=swap" rel="stylesheet">
<style>
:root{
  --ink:#111;
  --forest:#1b2e1a;
  --forest-deep:#142414;
  --green:#2c8a3c;
  --lime:#6fbf3a;
  --leaf:#8cc63f;
  --yellow:#ffd000;
  --cream:#f5f5ec;
  --white:#fff;
  --muted:#c9d2c5;
  --line:#d9d9cf;
}
*{box-sizing:border-box;margin:0;padding:0}
html,body{width:1200px;height:4093px;overflow:hidden}
body{font-family:"Figtree",sans-serif;color:var(--ink);background:var(--white);position:relative}
section,header,footer{position:absolute;left:0;width:1200px}
.abs{position:absolute}
.eyebrow{font-size:9px;font-weight:800;letter-spacing:2px;color:var(--lime);text-transform:uppercase}
.btn{display:inline-flex;align-items:center;justify-content:center;border-radius:30px;background:linear-gradient(90deg,#6fbf3a,#2c8a3c);color:#fff;font-weight:700;font-size:14px}

/* hero */
.hero{top:0;height:536px;background:#fff;overflow:hidden}
.hero-photo{left:590px;top:0;width:610px;height:536px;background:linear-gradient(135deg,#3d4a5c,#7f8ea3 45%,#c9a26b 70%,#2c3440)}
.hero-curve{left:0;top:0}
.brand{display:flex;align-items:center;gap:8px;font-weight:800;font-size:22px;color:var(--ink)}
.brand .dot{width:14px;height:14px;border-radius:50%;background:var(--yellow)}
.nav{left:356px;top:24px;display:flex;gap:22px;font-size:13px;font-weight:600}
.phone{left:728px;top:24px;font-size:13px;font-weight:600;display:flex;gap:6px;align-items:center;color:#fff}
.cta-top{left:876px;top:13px;width:164px;height:42px;font-size:13px}
.hero h1{left:156px;top:138px;font-size:46px;line-height:53px;font-weight:800;letter-spacing:-.5px}
.hero h1 em{font-style:normal;color:var(--lime)}
.hero .lede{left:156px;top:312px;font-size:14px;line-height:22px;width:360px}
.hero .btn{left:156px;top:382px;width:188px;height:51px}
.badge{left:598px;top:322px;width:146px;height:146px;border-radius:50%;background:var(--yellow);border:6px solid #fff;box-shadow:0 4px 12px rgba(0,0,0,.2);display:flex;align-items:center;justify-content:center;text-align:center;font-weight:700;font-size:17px;line-height:21px}

/* approach */
.approach{top:536px;height:466px;background:var(--forest);color:#fff}
.approach h2{left:158px;top:118px;font-size:34px;line-height:40px;font-weight:700;width:380px}
.approach .eyebrow{left:158px;top:103px}
.approach p.body{left:158px;top:254px;width:380px;font-size:12.5px;line-height:22px;color:#e8ece6}
.feature{left:632px;display:flex;gap:20px;width:390px}
.feature .ic{width:70px;height:64px;border-radius:10px;background:var(--yellow);flex:none;display:flex;align-items:center;justify-content:center}
.feature h3{font-size:20px;font-weight:700;margin-top:2px}
.feature p{font-size:12px;line-height:21px;color:#e8ece6;margin-top:4px}

/* services */
.services{top:1002px;height:737px;background:var(--cream)}
.services .eyebrow{left:0;width:1200px;text-align:center;top:102px}
.services h2{left:0;width:1200px;text-align:center;top:112px;font-size:34px;font-weight:700}
.svc{width:294px;height:237px;padding:20px 38px}
.svc svg{display:block;margin-bottom:18px}
.svc h3{font-size:19px;font-weight:700;margin-bottom:8px}
.svc p{font-size:12.5px;line-height:22px}
.svc.active{background:#fff;box-shadow:0 6px 20px rgba(0,0,0,.08)}
.vline{width:1px;background:var(--line)}
.hline{height:1px;background:var(--line)}

/* split */
.split{top:1739px;height:459px;background:var(--green);color:#fff;overflow:hidden}
.split-photo{left:0;top:0}
.split .eyebrow{left:658px;top:97px;color:var(--leaf)}
.split h2{left:658px;top:110px;font-size:34px;line-height:39px;font-weight:700;width:400px}
.split p{left:658px;top:244px;width:396px;font-size:12.5px;line-height:22px}

/* testimonials */
.testimonials{top:2198px;height:765px;background:#fff;overflow:hidden}
.testimonials .eyebrow{left:0;width:1200px;text-align:center;top:102px}
.testimonials h2{left:0;width:1200px;text-align:center;top:112px;font-size:34px;font-weight:700}
.quote-card{left:113px;top:173px;width:816px;height:367px;background:var(--leaf);border-radius:16px}
.quote-card blockquote{position:absolute;left:55px;top:60px;width:440px;font-size:26px;line-height:35px;font-weight:600;color:#1f5e26}
.quote-card cite{position:absolute;left:55px;top:262px;font-style:normal;font-size:14px;line-height:18px;color:#1f5e26}
.quote-photo{left:686px;top:248px;width:345px;height:217px;border-radius:10px;background:linear-gradient(135deg,#2a2a2a,#7a7570 55%,#bdb6ad)}
.landscape{left:0;top:500px;width:1200px;height:265px}

/* contact */
.contact{top:2963px;height:987px;background:var(--forest);color:#fff}
.contact .eyebrow{left:0;width:1200px;text-align:center;top:118px;color:var(--leaf)}
.contact h2{left:0;width:1200px;text-align:center;top:134px;font-size:34px;line-height:40px;font-weight:700}
.field{border:1px solid #6f7c6c;border-radius:4px;font-size:11.5px;color:#aab4a7;padding:22px 20px}
.field.focus{border:2px solid var(--leaf);color:#fff}
.contact .btn{left:480px;top:569px;width:240px;height:52px}
.info{width:220px;text-align:center}
.info .ic{width:70px;height:66px;margin:0 auto 18px;background:var(--yellow);border-radius:6px;display:flex;align-items:center;justify-content:center}
.info h3{font-size:16px;font-weight:700;margin-bottom:4px}
.info p{font-size:12.5px;line-height:22px}

/* footer */
.site-footer{top:3950px;height:143px;background:var(--forest-deep);color:#fff}
.site-footer .brand{left:140px;top:62px;color:#fff;position:absolute}
.socials{right:160px;top:48px;display:flex;gap:8px}
.socials span{width:11px;height:11px;border-radius:50%;background:var(--leaf)}
.legal{right:160px;top:68px;text-align:right;font-size:9px;line-height:15px;color:#aab4a7}
</style>
</head>
<body>

<header class="hero">
  <div class="abs hero-photo" role="img" aria-label="Smiling team of advisors working at computers in a bright office"></div>
  <svg class="abs hero-curve" width="1200" height="536" viewBox="0 0 1200 536" aria-hidden="true">
    <path d="M0 0 H620 C575 150 585 380 650 536 H0 Z" fill="#fff"/>
    <path d="M620 0 C575 150 585 380 650 536 H610 C550 380 555 150 595 0 Z" fill="#6fbf3a"/>
  </svg>
  <div class="abs brand" style="left:140px;top:18px"><span class="dot"></span>LUMORA</div>
  <nav class="abs nav"><span>Home</span><span>Services</span><span>About</span><span>Pricing</span></nav>
  <div class="abs phone">
    <svg width="14" height="14" viewBox="0 0 24 24"><circle cx="12" cy="12" r="11" fill="none" stroke="#ffd000" stroke-width="2"/><path d="M8 6l2 3-1.5 1.5a8 8 0 004 4L14 13l3 2-1 2.5C11 18 6 13 6.5 8z" fill="#ffd000"/></svg>
    (555) 014-0302
  </div>
  <a class="abs btn cta-top">Free Consultation</a>
  <h1 class="abs">Why settle for less<br>when your finances<br>could be <em>Exact?</em></h1>
  <p class="abs lede">Everything you and your business needs, so no more extra bills, or unwelcome surprises.</p>
  <a class="abs btn">See Our Services</a>
  <div class="abs badge">Business<br>advisors and<br>consultants</div>
</header>

<section class="approach">
  <span class="abs eyebrow">A fresh approach</span>
  <h2 class="abs">A fresh, all inclusive and simple approach to accounting</h2>
  <p class="abs body">Phasellus felis est, condimentum eget dolor non, hendrerit eleifend est. Mauris nunc ligula, laoreet nec odio eget, posuere porta quam. Nam efficitur vulputate nunc eu facilisis. Praesent lectus eros, auctor eget nunc sit amet, fringilla vestibulum tortor. Ut quis dapibus erat.</p>
  <div class="abs feature" style="top:102px">
    <div class="ic"><svg width="36" height="36" viewBox="0 0 36 36" fill="none" stroke="#1b2e1a" stroke-width="2"><circle cx="14" cy="14" r="7"/><circle cx="24" cy="24" r="7"/><path d="M24 20v4l3 2"/></svg></div>
    <div><h3>Experienced</h3><p>Phasellus felis est, condimentum eget dolor non, hendrerit eleifend est.</p></div>
  </div>
  <div class="abs feature" style="top:200px">
    <div class="ic"><svg width="36" height="36" viewBox="0 0 36 36" fill="none" stroke="#1b2e1a" stroke-width="2"><circle cx="13" cy="11" r="4"/><circle cx="23" cy="11" r="4"/><path d="M6 28c0-6 4-9 7-9s7 3 7 9M16 28c0-6 4-9 7-9s7 3 7 9"/></svg></div>
    <div><h3>Professional</h3><p>Mauris nunc ligula, laoreet odio eget, posuere porta quam efficitur vulputate nunc</p></div>
  </div>
  <div class="abs feature" style="top:298px">
    <div class="ic"><svg width="36" height="36" viewBox="0 0 36 36" fill="none" stroke="#1b2e1a" stroke-width="2"><circle cx="20" cy="12" r="7"/><path d="M20 8v8M17 10h5M17 14h5"/><path d="M4 26h8l6 3 12-6"/></svg></div>
    <div><h3>Affordable</h3><p>Nam efficitur vulputate facilisis praesent elit lectus eros, auctor eget nunc sit amet.</p></div>
  </div>
</section>

<section class="services">
  <span class="abs eyebrow">What we do</span>
  <h2 class="abs">Our Services</h2>
  <div class="abs vline" style="left:452px;top:173px;height:474px"></div>
  <div class="abs vline" style="left:746px;top:173px;height:236px"></div>
  <div class="abs hline" style="left:158px;top:409px;width:588px"></div>

  <article class="abs svc" style="left:158px;top:173px">
    <svg width="36" height="44" viewBox="0 0 36 44" fill="none" stroke="#2c8a3c" stroke-width="2"><rect x="4" y="3" width="28" height="38" rx="2"/><path d="M10 12h16M10 18h16M10 24h16M10 30h10"/></svg>
    <h3>Book Keeping</h3><p>Take the hassle out of managing your finances with our professional bookkeeping services.</p>
  </article>
  <article class="abs svc" style="left:452px;top:173px">
    <svg width="48" height="44" viewBox="0 0 48 44" fill="none" stroke="#2c8a3c" stroke-width="2"><rect x="14" y="3" width="30" height="30"/><path d="M18 10h22M20 20h18M20 26h18"/><circle cx="14" cy="32" r="9"/><path d="M14 27v10"/></svg>
    <h3>Taxes</h3><p>Expert guidance, maximum refunds, timely filing, and peace of mind. Our tax services are reliable for both Individuals and Businesses</p>
  </article>
  <article class="abs svc" style="left:746px;top:173px">
    <svg width="48" height="44" viewBox="0 0 48 44" fill="none" stroke="#2c8a3c" stroke-width="2"><path d="M4 4v36h40"/><path d="M12 38V28M20 38V22M28 38V18M36 38V12"/><path d="M8 26l12-10 8 4 14-14"/></svg>
    <h3>IPO Readiness Services</h3><p>Strategic planning, financial readiness, compliance and regulatory guidance, due diligence support, and investor relations, all to ensure your IPO is successful.</p>
  </article>
  <article class="abs svc" style="left:158px;top:410px">
    <svg width="48" height="44" viewBox="0 0 48 44" fill="none" stroke="#2c8a3c" stroke-width="2"><rect x="4" y="12" width="40" height="26" rx="2"/><path d="M17 12V6h14v6M4 22h40M14 18v8M34 18v8"/></svg>
    <h3>Fractional CFO</h3><p>Expert financial advice, strategic financial planning, budgeting and forecasting, and cash flow management to optimize your financial performance and drive growth.</p>
  </article>
  <article class="abs svc" style="left:452px;top:410px">
    <svg width="48" height="44" viewBox="0 0 48 44" fill="none" stroke="#2c8a3c" stroke-width="2"><path d="M6 3h22l6 6v30H6z"/><circle cx="24" cy="24" r="9"/><path d="M31 31l10 10"/><path d="M12 10h12"/></svg>
    <h3>Financial Reporting</h3><p>Timely &amp; accurate data, customized reporting, comprehensive analysis, all with clear concise presentation tailored for your business needs.</p>
  </article>
  <article class="abs svc active" style="left:746px;top:410px">
    <svg width="48" height="44" viewBox="0 0 48 44" fill="none" stroke="#2c8a3c" stroke-width="2"><rect x="4" y="6" width="30" height="34" rx="2"/><path d="M9 12h20M9 20h6M18 20h6M9 27h6M18 27h6M9 34h6M18 34h6"/><rect x="28" y="4" width="14" height="20"/><path d="M35 8v12"/></svg>
    <h3>Full Service Payroll</h3><p>Streamline your payroll with our reliable services. Accurate Calculations, Timely Payments, and Expert Tax Compliance</p>
  </article>
</section>

<section class="split">
  <svg class="abs split-photo" width="640" height="459" viewBox="0 0 640 459" role="img" aria-label="Business advisors reviewing documents with a client in a modern office">
    <defs><linearGradient id="officeTone" x1="0" y1="0" x2="1" y2="1"><stop offset="0" stop-color="#4a4a48"/><stop offset=".5" stop-color="#8f8a82"/><stop offset="1" stop-color="#3c3631"/></linearGradient></defs>
    <path d="M0 0H618C575 120 560 320 555 459H0Z" fill="url(#officeTone)"/>
    <path d="M618 0C575 120 560 320 555 459H575C580 320 595 120 640 0Z" fill="#6fbf3a"/>
  </svg>
  <span class="abs eyebrow">A fresh approach</span>
  <h2 class="abs">A fresh, all inclusive and simple approach to accounting</h2>
  <p class="abs">Phasellus felis est, condimentum eget dolor non, hendrerit eleifend. Mauris nunc ligula, laoreet nec odio eget, posuere porta quam. Nam efficitur vulputate nunc facilisis. Praesent lectus eros, auctor eget nunc sit amet, fringilla vestibulum tortor. Ut quis dapibus erat.</p>
</section>

<section class="testimonials">
  <span class="abs eyebrow">Word from our clients</span>
  <h2 class="abs">Client testimonials</h2>
  <div class="abs landscape" role="img" aria-label="Illustrated green hills with trees in front of a pale city skyline and a rising sun" style="background:linear-gradient(180deg,#fff 0%,#eef6e6 35%,#b9dca0 60%,#3f9a3a 85%,#1b2e1a 100%)"></div>
  <div class="abs quote-card">
    <blockquote>‘Many technology employees were gravitating naturally to Clearbook. So we followed our users to what has become one of our most important tools.’</blockquote>
    <cite>Rafe Dunmore<br>Communications expert, UK</cite>
  </div>
  <div class="abs quote-photo" role="img" aria-label="Portrait of a smiling client"></div>
</section>

<section class="contact">
  <span class="abs eyebrow">Contact us</span>
  <h2 class="abs">Get started with us and be<br>ready for excellent accounting</h2>
  <div class="abs field focus" style="left:158px;top:250px;width:430px;height:62px">First Name *</div>
  <div class="abs field" style="left:610px;top:250px;width:430px;height:62px">Last Name *</div>
  <div class="abs field" style="left:158px;top:328px;width:430px;height:62px">Work Email *</div>
  <div class="abs field" style="left:610px;top:328px;width:430px;height:62px">Company *</div>
  <div class="abs field" style="left:158px;top:406px;width:882px;height:134px">Message (Optional)</div>
  <a class="abs btn">Get my FREE Consulation</a>

  <div class="abs info" style="left:267px;top:697px">
    <div class="ic"><svg width="34" height="34" viewBox="0 0 34 34" fill="none" stroke="#1b2e1a" stroke-width="2"><path d="M4 14h20v12H4zM24 14a6 6 0 0112 0v12h-12"/><path d="M14 26v6M14 4v10M14 4h6v4h-6"/></svg></div>
    <h3>Office</h3><p>P.O. Box 4410<br>Cedar Hollow, ST 00000</p>
  </div>
  <div class="abs info" style="left:490px;top:697px">
    <div class="ic"><svg width="34" height="34" viewBox="0 0 34 34" fill="none" stroke="#1b2e1a" stroke-width="2"><circle cx="17" cy="17" r="14"/><path d="M11 10l3 4-2 2a9 9 0 006 6l2-2 4 3-2 3C15 26 8 19 8 12z"/></svg></div>
    <h3>Phone</h3><p>(555) 013-6971<br>(555) 014-0302</p>
    <h3 style="margin-top:20px">Fax</h3><p>(555) 017-3373</p>
  </div>
  <div class="abs info" style="left:712px;top:697px">
    <div class="ic"><svg width="34" height="34" viewBox="0 0 34 34" fill="none" stroke="#1b2e1a" stroke-width="2"><rect x="4" y="10" width="26" height="18" rx="2"/><path d="M4 12l13 9 13-9"/></svg></div>
    <h3>Email Address</h3><p>hello@lumora.example<br>www.lumora.example</p>
  </div>
</section>

<footer class="site-footer">
  <div class="brand"><span class="dot"></span>LUMORA</div>
  <div class="abs socials"><span></span><span></span><span></span><span></span><span></span></div>
  <div class="abs legal">Copyright © 2023 Lumora<br>Partners | Terms &amp; Conditions | Privacy Policy</div>
</footer>

</body>
</html>
```